Charting the steady harbor route is a show dedicated to helping plan fiduciaries close the gap between ERISA participant disclosures and employees, understanding, and attaining actual knowledge of their plan.

Target Market(s)

Retirement Plan Sponsors

Industry/Entity Type

Financial

Colors
0054AA
0677BA
7BADD7
CADEEF
E8F1F8

Requirements
Must have
• Charting the Steady Harbor Route

```html
<!DOCTYPE html>
<html lang="en">
<head>
<meta charset="utf-8">
<title>Charting the Steady Harbor Route Podcast</title>
<link href="https://fonts.googleapis.com/css2?family=Oswald:wght@500;600;700&display=swap" rel="stylesheet">
<style>
  :root {
    --page-bg: #cfddee;
    --band-blue: #4678b9;
    --frame-white: #ffffff;
    --tag-blue: #7badd7;
    --tag-text: #3f70b2;
    --portrait-light: #e4e4e4;
    --portrait-mid: #8a8a8a;
    --portrait-dark: #2a2a2a;
    --text-shadow: rgba(10, 40, 90, .35);
  }
  * { margin: 0; padding: 0; box-sizing: border-box; }
  html, body {
    width: 1200px; height: 447px; overflow: hidden;
    background: var(--page-bg);
  }
  .banner {
    position: absolute; left: 108px; top: 94px;
    width: 992px; height: 248px;
    background: var(--band-blue);
    overflow: hidden;
  }
  .banner-art { position: absolute; inset: 0; }
  .title-lines {
    position: absolute; left: 40px; top: 57px;
    width: 410px;
    text-align: right;
    white-space: nowrap;
    font-family: "Oswald", sans-serif;
    font-weight: 700; color: #fff;
    font-size: 56px; line-height: 54px;
    text-transform: uppercase;
    text-shadow: 3px 4px 6px var(--text-shadow);
  }
  .title-lines span { display: block; }
  .title-big {
    position: absolute; left: 462px; top: 47px;
    white-space: nowrap;
    font-family: "Oswald", sans-serif;
    font-weight: 700; color: #fff;
    font-size: 120px; line-height: 120px;
    text-shadow: 4px 5px 8px var(--text-shadow);
  }
  .host {
    position: absolute; left: 40px; top: 170px;
    width: 410px;
    text-align: right;
    white-space: nowrap;
    font-family: "Oswald", sans-serif;
    font-weight: 500; color: #fff;
    font-size: 27px; line-height: 30px;
    letter-spacing: 1px;
    text-shadow: 2px 3px 4px var(--text-shadow);
  }
  .tag {
    position: absolute; left: 462px; top: 176px;
    width: 122px; height: 23px;
    background: var(--tag-blue);
    color: var(--tag-text);
    font-family: "Oswald", sans-serif; font-weight: 600;
    font-size: 15px; line-height: 23px;
    letter-spacing: 7px; text-align: center;
    padding-left: 6px;
    white-space: nowrap;
  }
</style>
</head>
<body>
  <section class="banner">
    <svg class="banner-art" width="992" height="248" viewBox="0 0 992 248">
      <defs>
        <linearGradient id="portraitTone" x1="0" y1="0" x2="0" y2="1">
          <stop offset="0" stop-color="#e4e4e4"/>
          <stop offset=".55" stop-color="#8a8a8a"/>
          <stop offset="1" stop-color="#2a2a2a"/>
        </linearGradient>
      </defs>
      <rect class="inner-frame" x="25" y="25" width="880" height="199" fill="none" stroke="#ffffff" stroke-width="1.5"/>
      <polygon class="white-corner" points="886,0 992,0 992,248 730,248" fill="#fff"/>
      <path class="host-portrait" role="img" aria-label="Black and white portrait photo of the host in a dark suit and tie"
            d="M730,248 L760,218 Q790,200 815,190 L812,150 Q792,120 790,70 Q792,18 840,8 Q890,0 905,40 Q915,80 905,130 L895,160 L895,168 Q940,178 965,195 Q985,225 990,248 Z"
            fill="url(#portraitTone)"/>
    </svg>
    <h1 class="title-lines"><span>Charting the</span><span>Steady Harbor</span></h1>
    <div class="title-big">ROUTE</div>
    <div class="host">WITH NEIL VARDEN</div>
    <div class="tag">PODCAST</div>
  </section>
</body>
</html>
```